Carpentry company Needs a business card design

We need a design for a Carpentry / building company, business card. Please think of designs out of the ordinary and try to make it eye catching. Our existing logo will need to be incorporated in the design. However feel free to change the colours of the logo to suit your design. I would like to see some designs with green /black and orange incorporated into it.These are not the only colours accepted and all designs that appeal will be accepted.

Please contact me should you have any questions
Thanks Marcus

Target Market(s)

General Public seeking carpentry work

Industry/Entity Type

Business

Contact Information for Business Card

- Current company logo ( colours can be changed)
-Phone number ,
- info@brantelworks.com.au
- brantelworks.com.au
-@brantelworks social

Font styles to use
Other font styles liked:
• You choose

Requirements
Must have
• Services we provide
• - Renovations
• -Deckings & Pergolas
• -Kitchens
• - Bathrooms
• - Intricate details
Nice to have
• an awesome design
Should not have
• Tools on the business card

```html
<!DOCTYPE html>
<html lang="en">
<head>
<meta charset="utf-8">
<title>Brantel Works – Business Card</title>
<link rel="stylesheet" href="https://fonts.googleapis.com/css2?family=Questrial&display=swap">
<style>
  :root {
    --backdrop: #e4e4e2;
    --card-black: #151515;
    --card-orange: #f2420e;
    --accent: #f2420e;
    --ink-light: #f4f4f4;
    --ink-soft: #bdbdbd;
    --ink-dark: #1a1a1a;
  }
  * { margin: 0; padding: 0; box-sizing: border-box; }
  html, body {
    width: 1200px; height: 1021px; overflow: hidden;
    background: var(--backdrop);
    font-family: "Questrial", "Century Gothic", sans-serif;
  }
  .canvas { position: relative; width: 1200px; height: 1021px; }
  .card {
    position: absolute; width: 520px; height: 300px;
    box-shadow: 0 14px 30px rgba(0,0,0,.22);
    overflow: hidden;
  }
  .card--front { left: 70px; top: 170px; background: var(--card-black); }
  .card--back { left: 610px; top: 540px; background: var(--card-orange); }
  .card__lines { position: absolute; inset: 0; }
  .brand {
    position: absolute; display: flex; align-items: center; gap: 12px;
    color: var(--ink-light); font-size: 30px; letter-spacing: 4px;
    white-space: nowrap;
  }
  .brand__mark { width: 13px; height: 13px; background: var(--accent); }
  .card--front .brand { left: 50%; top: 94px; transform: translateX(-50%); }
  .card--back .brand { right: 40px; top: 72px; }
  .card--back .brand__mark { background: var(--ink-dark); }
  .contact {
    position: absolute; left: 0; right: 0; top: 190px;
    display: flex; flex-direction: column; align-items: center; gap: 10px;
    color: var(--ink-soft); font-size: 13px; letter-spacing: .3px;
  }
  .contact__row { display: flex; gap: 26px; }
  .contact__item { display: flex; align-items: center; gap: 7px; }
  .contact__icon { width: 12px; height: 12px; flex: none; }
  .contact__square { width: 10px; height: 10px; background: var(--accent); }
  .services {
    position: absolute; left: 44px; bottom: 40px; list-style: none;
    color: var(--ink-light); font-size: 15px; letter-spacing: .3px;
  }
  .services__item { display: flex; align-items: center; gap: 8px; margin-top: 8px; }
  .services__tick { width: 12px; height: 12px; flex: none; }
</style>
</head>
<body>
<main class="canvas">

  <section class="card card--front" aria-label="Card front">
    <svg class="card__lines" viewBox="0 0 520 300" aria-hidden="true">
      <line x1="250" y1="36" x2="520" y2="14" stroke="#f2420e" stroke-width="2"/>
      <line x1="90" y1="0" x2="14" y2="300" stroke="#f2420e" stroke-width="2"/>
    </svg>
    <div class="brand"><span class="brand__mark"></span><span class="brand__name">BRANTEL WORKS</span></div>
    <div class="contact">
      <div class="contact__row">
        <span class="contact__item">
          <svg class="contact__icon" viewBox="0 0 12 12" aria-hidden="true"><rect x="1" y="2.5" width="10" height="7" fill="none" stroke="#f2420e" stroke-width="1.2"/><polyline points="1,2.5 6,6.5 11,2.5" fill="none" stroke="#f2420e" stroke-width="1.2"/></svg>
          info@brantelworks.com.au
        </span>
        <span class="contact__item">
          <svg class="contact__icon" viewBox="0 0 12 12" aria-hidden="true"><circle cx="6" cy="6" r="5" fill="none" stroke="#f2420e" stroke-width="1.2"/><ellipse cx="6" cy="6" rx="2.2" ry="5" fill="none" stroke="#f2420e" stroke-width="1"/><line x1="1" y1="6" x2="11" y2="6" stroke="#f2420e" stroke-width="1"/></svg>
          brantelworks.com.au
        </span>
      </div>
      <span class="contact__item"><span class="contact__square"></span>@brantelworks social</span>
    </div>
  </section>

  <section class="card card--back" aria-label="Card back">
    <div class="brand"><span class="brand__mark"></span><span class="brand__name">BRANTEL WORKS</span></div>
    <ul class="services">
      <li class="services__item"><svg class="services__tick" viewBox="0 0 12 12" aria-hidden="true"><rect x=".6" y=".6" width="10.8" height="10.8" fill="none" stroke="#fff" stroke-width="1"/><polyline points="2.5,6 5,8.5 9.5,3" fill="none" stroke="#fff" stroke-width="1.6"/></svg>Renovations</li>
      <li class="services__item"><svg class="services__tick" viewBox="0 0 12 12" aria-hidden="true"><rect x=".6" y=".6" width="10.8" height="10.8" fill="none" stroke="#fff" stroke-width="1"/><polyline points="2.5,6 5,8.5 9.5,3" fill="none" stroke="#fff" stroke-width="1.6"/></svg>Deckings &amp; Pergolas</li>
      <li class="services__item"><svg class="services__tick" viewBox="0 0 12 12" aria-hidden="true"><rect x=".6" y=".6" width="10.8" height="10.8" fill="none" stroke="#fff" stroke-width="1"/><polyline points="2.5,6 5,8.5 9.5,3" fill="none" stroke="#fff" stroke-width="1.6"/></svg>Kitchens</li>
      <li class="services__item"><svg class="services__tick" viewBox="0 0 12 12" aria-hidden="true"><rect x=".6" y=".6" width="10.8" height="10.8" fill="none" stroke="#fff" stroke-width="1"/><polyline points="2.5,6 5,8.5 9.5,3" fill="none" stroke="#fff" stroke-width="1.6"/></svg>Bathrooms</li>
      <li class="services__item"><svg class="services__tick" viewBox="0 0 12 12" aria-hidden="true"><rect x=".6" y=".6" width="10.8" height="10.8" fill="none" stroke="#fff" stroke-width="1"/><polyline points="2.5,6 5,8.5 9.5,3" fill="none" stroke="#fff" stroke-width="1.6"/></svg>Intricate details</li>
    </ul>
  </section>

</main>
</body>
</html>
```